Business Card & Stationary
For Event Planning Website
I need single sided standard sized Business Card [3.5" x 2"]
Same as logo or similar
Professional
First Name Last Name
Founder & Chief Executive Officer
Address 1
Address 2
Harlow Bay, NY 10482
xyz@juniperhours.com
www.juniperhours.com
Feel free to be creative - the site is for party planning (weddings, bar-mitzvahs, etc.) so it should be modern & professional, with a fun factor.
I used test data to protect personal data but I can supply you with all of the information you need later.
I'm not sure which eps file corresponds to the jpg.
This is the hamsa (hand) which is part of the logo
The hand - ai file
Webpage Background Pattern

```html
<!DOCTYPE html>
<html lang="en">
<head>
<meta charset="utf-8">
<title>Juniper Hours — Business Cards</title>
<link rel="stylesheet" href="https://fonts.googleapis.com/css2?family=Montserrat:wght@400&family=Arimo:wght@700&family=Courier+Prime&display=swap">
<style>
  :root {
    --brand-blue: #1f7fc3;
    --brand-blue-deep: #1a74b6;
    --ink-grey: #4a4f55;
    --title-blue: #4d9fd6;
    --card-white: #fbfcfd;
    --card-shade: #eef1f4;
    --motif-tint: #e3ebf3;
    --page: #e9e7e4;
    --white: #ffffff;
  }
  html, body {
    margin: 0;
    width: 1200px;
    height: 961px;
    overflow: hidden;
    background: var(--page);
  }
  .stage {
    position: relative;
    width: 1200px;
    height: 961px;
  }
  .card {
    position: absolute;
    width: 540px;
    height: 309px;
    overflow: hidden;
    box-shadow: 0 4px 12px rgba(0,0,0,0.18);
  }
  .card--front {
    background: linear-gradient(160deg, var(--card-white), var(--card-shade));
  }
  .card--back { background: var(--brand-blue-deep); }
  .card--front-top { left: 30px; top: 40px; }
  .card--back-mid { left: 630px; top: 290px; }
  .card--front-bottom { left: 30px; top: 590px; }

  .motif {
    position: absolute;
    border-radius: 48% 48% 40% 40%;
    background: radial-gradient(ellipse at center, var(--motif-tint), rgba(227,235,243,0) 75%);
  }
  .pattern-fill {
    position: absolute;
    inset: 0;
    background: radial-gradient(circle at 30% 40%, #2585c8, var(--brand-blue-deep) 70%);
  }

  .wordmark {
    position: absolute;
    margin: 0;
    font-family: "Montserrat", sans-serif;
    font-weight: 400;
    font-size: 60px;
    line-height: 1;
    letter-spacing: -1px;
    color: var(--brand-blue);
  }
  .card--back .wordmark { color: var(--white); }
  .mark-dot {
    position: absolute;
    width: 44px;
    height: 44px;
    border-radius: 50%;
    border: 3px solid var(--brand-blue);
    box-sizing: border-box;
  }
  .card--back .mark-dot { border-color: var(--white); }

  .person-name {
    position: absolute;
    margin: 0;
    font-family: "Arimo", sans-serif;
    font-weight: 700;
    font-size: 22px;
    line-height: 1.2;
    color: var(--brand-blue);
  }
  .person-title {
    position: absolute;
    margin: 0;
    font-family: "Courier Prime", monospace;
    font-size: 14px;
    line-height: 1.2;
    color: var(--title-blue);
  }
  .contact {
    position: absolute;
    margin: 0;
    font-family: "Courier Prime", monospace;
    font-style: normal;
    font-size: 14px;
    line-height: 18px;
    color: var(--ink-grey);
  }
  .contact .gap { display: block; height: 18px; }
</style>
</head>
<body>
<main class="stage">

  <section class="card card--front card--front-top">
    <div class="motif" role="img" aria-label="Faint hand motif watermark" style="left:22px; top:96px; width:160px; height:205px;"></div>
    <h1 class="wordmark" style="left:20px; top:14px;">juniperhours</h1>
    <div class="mark-dot" style="left:478px; top:22px;"></div>
    <p class="person-name" style="left:22px; top:104px;">Hadley A. Tolbrek</p>
    <p class="person-title" style="left:22px; top:132px;">Founder &amp; Chief Executive Officer</p>
    <address class="contact" style="left:225px; top:160px;">
      Address 1<br>Address 2<br>Harlow Bay, NY 10482
      <span class="gap"></span>
      (212) 555-0148<br>xyz@juniperhours.com<br>www.juniperhours.com
    </address>
  </section>

  <section class="card card--back card--back-mid">
    <div class="pattern-fill" role="img" aria-label="Tonal blue hand-motif background pattern"></div>
    <h2 class="wordmark" style="left:40px; top:122px;">juniperhours</h2>
    <div class="mark-dot" style="left:472px; top:130px;"></div>
  </section>

  <section class="card card--front card--front-bottom">
    <div class="motif" role="img" aria-label="Faint hand motif watermark" style="left:42px; top:58px; width:190px; height:240px;"></div>
    <h2 class="wordmark" style="left:22px; top:30px;">juniperhours</h2>
    <div class="mark-dot" style="left:478px; top:100px;"></div>
    <address class="contact" style="left:312px; top:150px;">
      Address 1<br>Address 2<br>Harlow Bay, NY 10482
      <span class="gap"></span>
      (212) 555-0148<br>xyz@juniperhours.com<br>www.juniperhours.com
    </address>
    <p class="person-name" style="left:22px; top:244px;">Hadley A. Tolbrek</p>
    <p class="person-title" style="left:22px; top:272px; font-size:13px;">Founder &amp; Chief Executive Officer</p>
  </section>

</main>
</body>
</html>
```